Marnie's Fitness Business Cards

I would like my business cards to look expensive and sophisticated using my logo and the information below.

FRONT
Marnie’s Fitness logo

Tag line Become your happiest, healthiest and strongest self

Marnie Pulham Crisp
Personal Trainer

e. marnie@marniesfitness.example

t. 0781350462

w. www.marniesfitness.example

```html
<!DOCTYPE html>
<html lang="en">
<head>
<meta charset="utf-8">
<title>Marnie's Fitness Business Cards</title>
<link href="https://fonts.googleapis.com/css2?family=Montserrat:wght@300;400;500;600&display=swap" rel="stylesheet">
<style>
  :root {
    --backdrop: #141414;
    --card: #0c0c0d;
    --card-sheen: #1e1e20;
    --teal: #7fc6d2;
    --silver: #cfc4c2;
    --ink-light: #e6e6e6;
    --rule: #9a9a9a;
  }
  * { margin: 0; padding: 0; box-sizing: border-box; }
  html, body {
    width: 1200px; height: 864px; overflow: hidden;
    background: var(--backdrop);
    font-family: "Montserrat", sans-serif;
  }
  .canvas { position: relative; width: 1200px; height: 864px; }
  .card {
    position: absolute; width: 560px; height: 320px;
    background: linear-gradient(150deg, var(--card-sheen) 0%, var(--card) 45%, var(--card) 100%);
    box-shadow: 0 18px 40px rgba(0,0,0,.6);
    overflow: hidden;
  }

  /* Brand side */
  .card--brand { left: 560px; top: 120px; }
  .brand-mark {
    position: absolute; left: 44px; top: 50px;
    width: 200px; height: 200px; border-radius: 50%;
    border: 3px solid var(--teal);
  }
  .brand-name {
    position: absolute; left: 266px; top: 112px; width: 270px;
    font-size: 26px; font-weight: 400; letter-spacing: 4px; line-height: 32px;
    color: var(--teal); text-transform: uppercase;
  }
  .brand-name span { display: block; white-space: nowrap; }
  .tagline {
    position: absolute; left: 266px; top: 196px; width: 270px;
    font-size: 12px; font-weight: 400; letter-spacing: 2px; line-height: 20px;
    color: var(--ink-light); text-transform: uppercase;
  }

  /* Contact side */
  .card--contact { left: 80px; top: 470px; }
  .contact-brand {
    position: absolute; right: 40px; top: 40px;
    display: flex; align-items: center; gap: 10px;
  }
  .contact-brand__dot {
    width: 26px; height: 26px; border-radius: 50%;
    border: 2px solid var(--teal);
  }
  .contact-brand__name {
    font-size: 14px; font-weight: 400; letter-spacing: 3px; white-space: nowrap;
    color: var(--teal); text-transform: uppercase;
  }
  .divider {
    position: absolute; left: 0; top: 138px; width: 470px; height: 2px;
    background: linear-gradient(90deg, rgba(154,154,154,.2), var(--rule));
  }
  .person { position: absolute; right: 40px; top: 150px; text-align: right; }
  .person__name {
    font-size: 17px; font-weight: 400; letter-spacing: 1.5px; white-space: nowrap;
    color: var(--teal); text-transform: uppercase;
  }
  .person__role {
    display: inline-block; margin-top: 3px; padding-top: 2px;
    border-top: 1px solid var(--rule);
    font-size: 12px; font-weight: 500; color: var(--ink-light);
  }
  .contacts {
    position: absolute; right: 40px; top: 222px; list-style: none;
  }
  .contacts li {
    display: flex; justify-content: flex-end; align-items: center; gap: 10px;
    font-size: 13px; font-weight: 300; letter-spacing: .5px; white-space: nowrap;
    color: var(--ink-light); margin-bottom: 6px;
  }
  .contacts strong { font-weight: 600; }
  .contacts svg { width: 16px; height: 16px; flex: none; }
</style>
</head>
<body>
<div class="canvas">

  <section class="card card--brand">
    <div class="brand-mark"></div>
    <div class="brand-name"><span>Marnie's</span><span>Fitness</span></div>
    <p class="tagline">Become your happiest, healthiest and strongest self</p>
  </section>

  <section class="card card--contact">
    <div class="contact-brand">
      <span class="contact-brand__dot"></span>
      <span class="contact-brand__name">Marnie's Fitness</span>
    </div>
    <div class="divider"></div>
    <div class="person">
      <div class="person__name">Marnie Pulham Crisp</div>
      <div class="person__role">Personal Trainer</div>
    </div>
    <ul class="contacts">
      <li>0781350462
        <svg viewBox="0 0 16 16" aria-hidden="true"><circle cx="8" cy="8" r="7.5" fill="none" stroke="#7fc6d2"/><path d="M5.5 4.5l1.5 0 .6 2-1 .8a5 5 0 0 0 2.1 2.1l.8-1 2 .6v1.5c0 .4-.4.8-.8.8A6 6 0 0 1 4.7 5.3c0-.4.4-.8.8-.8z" fill="#7fc6d2"/></svg>
      </li>
      <li>marnie@marniesfitness.example
        <svg viewBox="0 0 16 16" aria-hidden="true"><circle cx="8" cy="8" r="7.5" fill="none" stroke="#7fc6d2"/><rect x="4" y="5.5" width="8" height="5.5" fill="none" stroke="#7fc6d2"/><path d="M4 5.5l4 3 4-3" fill="none" stroke="#7fc6d2"/></svg>
      </li>
      <li><span>www.<strong>marniesfitness</strong>.example</span>
        <svg viewBox="0 0 16 16" aria-hidden="true"><circle cx="8" cy="8" r="7.5" fill="none" stroke="#7fc6d2"/><circle cx="8" cy="8" r="3.8" fill="none" stroke="#7fc6d2"/><path d="M4.2 8h7.6M8 4.2c1.6 2.2 1.6 5.4 0 7.6M8 4.2c-1.6 2.2-1.6 5.4 0 7.6" fill="none" stroke="#7fc6d2" stroke-width=".8"/></svg>
      </li>
    </ul>
  </section>

</div>
</body>
</html>
```